Grubbits Feather Fiesta freeze-dried mealworm treats

"Grubbits" is the product name, "Feather Fiesta" is the product description name. Similar to Brando's "Wedgies" or "Garden Herb" chips, or like Vesta-Pop "Dawn" or "Nova". Feather Fiesta is descriptive of what's inside. I really wanted to call it "Beak Buzz" because if you have ever seen a bird's reaction to a live or dried mealworm you would understand the "mania" part. :-) I didn't feel that SOME would appreciate the association with crack though it is more descriptive than "mania" or the like. Birds are completely crazy over these worms and can be trained to sit on a feeder or otherwise and literally wait for their serving. This is why I requested "Feather Fiesta" to be in an "exciting" kind of font. I don't work with fonts but I figure a designer does. This project request is for a design that can be used for direct printing to bag packaging or for printed labels for using on buckets or plastic jars.
Updates

This is my first experience at getting my product label accomplished. Of my many talents, graphic design and creativity are at the bottom :-) After looking around here, I realize that I didn't give you much to work with so, I think I have a better idea of what you need and will provide more within a couple of days. Sorry...I'll get it right :-) and thanks!

We need to put this project on hold temporarily. I will post an update and additional project particulars soon.

Target Market(s)

Poultry owners, wild bird enthusiasts, small reptile pet owners

Font styles to use
Other font styles liked:
• Grubbits in Berkshire Swash but I am open. Feather Fiesta in something "exciting"

Colors

Designer to choose colors to be used in the design.

Requirements
Must have
• Editible. Must have the "made in the USA" info.
Nice to have
• A fun, colorful visual that includes fun wild birds and chicken(s) perhaps with a worm or worms in some beaks. The reptile graphic is not necessary as there are too many. The designer can suggest the font but "Grubbits" should be different from "Feather Fiesta" My uploaded file is basic but hopefully projects the idea. If I need to provide more graphics that I like (birds, chicks, etc) please let me know.

```html
<!DOCTYPE html>
<html lang="en">
<head>
<meta charset="utf-8">
<title>Grubbits Feather Fiesta – Freeze-Dried Mealworm Treats</title>
<link href="https://fonts.googleapis.com/css2?family=Alegreya:wght@700&family=Chewy&family=Lato:wght@400&display=swap" rel="stylesheet">
<style>
  :root {
    --page: #f2f2f0;
    --pack: #ffffff;
    --ink: #3a3a3a;
    --ink-soft: #555555;
    --lime: #d4e02a;
    --lime-shadow: #f2ee5a;
    --outline: #333333;
    --worm-light: #d9aa62;
    --worm-dark: #7a4f22;
    --bird-teal: #2f5560;
    --bird-orange: #e8a24a;
    --bird-red: #ee6b5f;
    --bird-blue: #2f6fb8;
    --flag-red: #c8323c;
    --flag-blue: #3a4a8a;
  }
  * { margin: 0; padding: 0; box-sizing: border-box; }
  html, body { width: 1200px; height: 1000px; overflow: hidden; }
  body { background: var(--page); font-family: "Lato", sans-serif; color: var(--ink); }

  .canvas { position: relative; width: 1200px; height: 1000px; }

  .pack {
    position: absolute; left: 190px; top: 55px; width: 565px; height: 885px;
    background: var(--pack); border-radius: 28px;
  }

  .bird-scene {
    position: absolute; left: 70px; top: 180px; width: 440px; height: 225px;
    border-radius: 40px;
    background: linear-gradient(100deg, var(--bird-blue) 0%, var(--bird-teal) 35%, var(--bird-orange) 60%, var(--bird-red) 82%, var(--lime) 100%);
    opacity: 0.85;
  }

  .brand {
    position: absolute; left: 0; width: 100%; top: 352px; text-align: center;
    font-family: "Alegreya", serif; font-weight: 700; font-size: 40px; color: var(--ink);
  }
  .brand-dot {
    display: inline-block; width: 14px; height: 14px; border-radius: 50%;
    background: var(--ink); margin-right: 8px; vertical-align: 6px;
  }

  .product-name {
    position: absolute; left: 0; width: 100%; top: 418px; text-align: center;
    font-family: "Chewy", cursive; font-size: 92px; line-height: 94px;
    color: var(--lime);
    -webkit-text-stroke: 3px var(--outline);
    paint-order: stroke fill;
    text-shadow: 6px 5px 0 var(--lime-shadow);
  }

  .benefits {
    position: absolute; left: 64px; top: 620px; font-size: 11px; line-height: 13px; color: var(--ink-soft);
  }
  .benefits ul { list-style: none; margin-top: 6px; }
  .benefits li { font-size: 16px; line-height: 24px; color: var(--ink); }
  .benefits li::before { content: "✔"; margin-right: 2px; }
  .benefits .more { font-size: 11px; margin-top: 2px; }

  .origin { position: absolute; left: 72px; top: 752px; width: 120px; }
  .flag {
    width: 32px; height: 22px; display: block;
    background: repeating-linear-gradient(180deg, var(--flag-red) 0 3px, #fff 3px 6px);
    position: relative;
  }
  .flag::after {
    content: ""; position: absolute; left: 0; top: 0; width: 14px; height: 11px; background: var(--flag-blue);
  }
  .origin p { margin-top: 8px; font-size: 8px; line-height: 9px; color: var(--ink-soft); }

  .contents {
    position: absolute; left: 180px; top: 632px; width: 162px; height: 162px; border-radius: 50%;
    background: radial-gradient(circle at 45% 40%, var(--worm-light) 0%, #b98240 55%, var(--worm-dark) 100%);
  }

  .freshness {
    position: absolute; left: 388px; top: 628px; width: 130px; text-align: center;
    font-size: 16px; line-height: 21px; color: var(--ink-soft);
  }
  .weight {
    position: absolute; left: 430px; top: 778px; font-size: 16px; color: var(--ink);
  }
</style>
</head>
<body>
<main class="canvas">
  <section class="pack">
    <div class="bird-scene" role="img" aria-label="Illustration of a rooster holding a mealworm in its beak, surrounded by a robin, a bluebird, a cardinal and a finch"></div>

    <div class="brand"><span class="brand-dot"></span>Grubbits</div>

    <h1 class="product-name">Feather<br>Fiesta</h1>

    <div class="benefits">
      Protein-packed<br>high-energy for
      <ul>
        <li>Poultry</li>
        <li>Wild Birds</li>
        <li>Pet Spider</li>
      </ul>
      <p class="more">and many more</p>
    </div>

    <div class="origin">
      <span class="flag" role="img" aria-label="United States flag"></span>
      <p>100% of our grubbits are grown and processed in the USA</p>
    </div>

    <div class="contents" role="img" aria-label="Photo of freeze-dried mealworms"></div>

    <p class="freshness">100%<br>freeze-dried<br>for maximum<br>freshness</p>

    <p class="weight">500g ℮</p>
  </section>
</main>
</body>
</html>
```